Keystone Plasterworks Business Card

Looking to update the imagery, colors and logo to a more current design and to reflect their specialty of "High End" residential home construction

```html
<!DOCTYPE html>
<html lang="en">
<head>
<meta charset="utf-8">
<title>Keystone Plasterworks Business Card</title>
<link rel="stylesheet" href="https://fonts.googleapis.com/css2?family=Montserrat:wght@600;700;800&family=Arimo:wght@400;700&display=swap">
<style>
  :root {
    --stage: #1d1d1f;
    --deep-blue: #14305a;
    --sky-blue: #2d6a9f;
    --navy: #14305a;
    --paper: #ffffff;
    --ink-blue: #1c3f70;
    --badge-one: #8fa3bb;
    --badge-two: #a9b8c9;
    --badge-three: #c3cfdc;
  }
  * { box-sizing: border-box; margin: 0; padding: 0; }
  html, body { width: 1200px; height: 1015px; overflow: hidden; background: var(--stage); }
  body { position: relative; font-family: "Arimo", Arial, sans-serif; }

  .card {
    position: absolute; left: 200px; width: 800px; height: 457px;
    background: var(--paper); overflow: hidden;
  }
  .card--back { top: 30px; }
  .card--front { top: 528px; }

  /* Back side */
  .services-residential {
    position: absolute; top: 0; left: 0; right: 0; height: 124px;
    background: var(--deep-blue); color: var(--paper);
    text-align: center; padding-top: 28px;
  }
  .services-heading {
    font-family: "Montserrat", sans-serif; font-weight: 800;
    font-size: 24px; letter-spacing: .5px; text-transform: uppercase;
  }
  .services-line { font-size: 23px; margin-top: 8px; }
  .services-commercial {
    position: absolute; top: 124px; left: 0; right: 0; height: 176px;
    background: var(--sky-blue); color: var(--paper); padding: 18px 0 0 90px;
  }
  .services-commercial .services-heading { text-align: left; padding-left: 60px; }
  .service-columns { display: flex; gap: 40px; margin-top: 8px; }
  .service-list { list-style: none; font-size: 22px; line-height: 27px; }
  .service-list li::before { content: "\2022"; margin-right: 12px; }
  .band-stripe {
    position: absolute; top: 300px; left: 0; right: 0; height: 8px; background: var(--deep-blue);
  }
  .supporters {
    position: absolute; top: 308px; left: 0; right: 0; bottom: 0;
    display: flex; flex-direction: column; align-items: center; padding-top: 18px;
  }
  .supporters-title {
    font-family: "Montserrat", sans-serif; font-weight: 800; font-size: 23px; color: var(--navy);
  }
  .badge-row { display: flex; gap: 60px; align-items: center; margin-top: 20px; }
  .badge { display: block; border-radius: 6px; }
  .badge--one { width: 170px; height: 56px; background: var(--badge-one); }
  .badge--two { width: 190px; height: 44px; background: var(--badge-two); }
  .badge--three { width: 110px; height: 60px; background: var(--badge-three); }

  /* Front side */
  .brand {
    position: absolute; top: 70px; right: 50px;
    display: flex; align-items: center; gap: 12px;
  }
  .brand-mark { width: 22px; height: 22px; background: var(--ink-blue); }
  .brand-name {
    font-family: "Montserrat", sans-serif; font-weight: 800; font-size: 40px; color: var(--ink-blue);
  }
  .brand-rule {
    position: absolute; top: 138px; right: 50px; width: 380px; height: 2px; background: var(--ink-blue);
  }
  .holder-name {
    position: absolute; top: 220px; left: 50px;
    font-family: "Montserrat", sans-serif; font-weight: 700; font-size: 32px;
    color: var(--ink-blue); letter-spacing: .5px;
  }
  .holder-rule {
    position: absolute; top: 268px; left: 50px; right: 50px; height: 2px; background: var(--ink-blue);
  }
  .contact {
    position: absolute; top: 286px; list-style: none; font-size: 22px; line-height: 32px; color: #1a1a1a;
  }
  .contact--phones { left: 50px; }
  .contact--online { left: 330px; }
  .contact li { display: flex; align-items: center; gap: 12px; }
  .contact svg { width: 22px; height: 22px; flex: none; }
  .footer-band {
    position: absolute; left: 0; bottom: 0; width: 320px; height: 40px; background: var(--deep-blue);
  }
  .tagline {
    position: absolute; right: 0; bottom: 0; width: 520px; height: 90px;
    background: var(--sky-blue); color: var(--paper);
    clip-path: polygon(4% 0, 100% 0, 100% 100%, 0 100%);
    padding: 20px 20px 0 50px;
    font-size: 19px; line-height: 25px; text-transform: uppercase; letter-spacing: .3px;
  }
</style>
</head>
<body>

<section class="card card--back" aria-label="Card back: services">
  <div class="services-residential">
    <h2 class="services-heading">Residential</h2>
    <p class="services-line">Drywall Installation &#8226; Drywall Finish</p>
  </div>
  <div class="services-commercial">
    <h2 class="services-heading">Commercial / Condo Towers</h2>
    <div class="service-columns">
      <ul class="service-list">
        <li>Light Gauge Metal Framing</li>
        <li>Wall and Ceiling Insulation</li>
        <li>Drywall Installation</li>
        <li>FRP</li>
      </ul>
      <ul class="service-list">
        <li>Drywall Finish</li>
        <li>Exterior Sheathing</li>
        <li>Acoustical Ceilings</li>
      </ul>
    </div>
  </div>
  <div class="band-stripe"></div>
  <div class="supporters">
    <p class="supporters-title">Proud Supporter</p>
    <div class="badge-row">
      <span class="badge badge--one" role="img" aria-label="Partner badge: home builders committee"></span>
      <span class="badge badge--two" role="img" aria-label="Partner badge: regional builders association"></span>
      <span class="badge badge--three" role="img" aria-label="Membership badge: remodeling association"></span>
    </div>
  </div>
</section>

<section class="card card--front" aria-label="Card front: contact">
  <div class="brand">
    <span class="brand-mark"></span>
    <span class="brand-name">Keystone Plasterworks</span>
  </div>
  <div class="brand-rule"></div>

  <h1 class="holder-name">DALE HARTWELL</h1>
  <div class="holder-rule"></div>

  <ul class="contact contact--phones">
    <li>
      <svg viewBox="0 0 24 24" aria-hidden="true"><path d="M6 3l4 4-2 3c1 2 3 4 5 5l3-2 4 4-3 3C10 20 4 14 3 6z" fill="none" stroke="var(--ink-blue)" stroke-width="2" stroke-linejoin="round"/></svg>
      (214) 555-0147
    </li>
    <li>
      <svg viewBox="0 0 24 24" aria-hidden="true"><rect x="6" y="2" width="12" height="20" rx="2" fill="none" stroke="var(--ink-blue)" stroke-width="2"/><line x1="10" y1="18" x2="14" y2="18" stroke="var(--ink-blue)" stroke-width="2"/></svg>
      (817) 555-0182
    </li>
  </ul>
  <ul class="contact contact--online">
    <li>
      <svg viewBox="0 0 24 24" aria-hidden="true"><rect x="2" y="5" width="20" height="14" fill="var(--ink-blue)"/><polyline points="2,5 12,13 22,5" fill="none" stroke="var(--paper)" stroke-width="2"/></svg>
      dale@keystoneplasterworks.com
    </li>
    <li>
      <svg viewBox="0 0 24 24" aria-hidden="true"><g fill="none" stroke="var(--ink-blue)" stroke-width="2"><circle cx="12" cy="12" r="10"/><ellipse cx="12" cy="12" rx="4" ry="10"/><line x1="2" y1="12" x2="22" y2="12"/></g></svg>
      www.keystoneplasterworks.com
    </li>
  </ul>

  <div class="footer-band"></div>
  <p class="tagline">Specializing in quality resedential &amp;<br>commercial interiors since 1982</p>
</section>

</body>
</html>
```